Corvane Partners Web Design

Dear all
I need a web design for a financial services site. We are a broker who deals with many different financial institutions and require a clean, simple and instantly impressive site based on the colour scheme that SketchGuild created for us. A landing page (www.crvnp.mx) gives an idea of the logo and clour scheme but we are looking at either a one page site with rollover text boxes or a 3 or 4 page site depending on the preference of the designer and the best user experience. The site“s purpose is to give confidence that the company exists rather than impart pages of information although we would like this to be a site that can expand over time as the company grows. For now the requirement is for a clear set of possibly changing images at the centre of a white screen that relate to finance in general nad the benefits of wealth creation as well as sectios either along the top or bottom - Our Company, Our Approach, Our services, Our clients, Contact (user to fill in contact box to be sent to info@crvnp.mx. The text for each of these boxes I assume can be added by the coding team here, it the overall look and feel that I am looking for from SketchGuild - deadline can be extended if necessary but I was hoping to wrap this all up in October

Target Market(s)

Succesful individuals looking to maximise returns on their investment via world class financial institutions and supported throughout by qualified independent financial advisors

Industry/Entity Type

Finance

Requirements
Must have
• Logo and color scheme of the logo design SketchGuild sent - I have all these sourcefiles, pantone and fonts

```html
<!DOCTYPE html>
<html lang="en">
<head>
<meta charset="utf-8">
<title>Corvane Partners</title>
<link href="https://fonts.googleapis.com/css2?family=Questrial&family=Exo+2:wght@700&family=Arimo:wght@400;700&display=swap" rel="stylesheet">
<style>
:root{
  --navy:#1f3763;
  --navy-soft:#2f4670;
  --orange:#f0901e;
  --text:#3a4660;
  --muted:#6d7688;
  --line:#d8d8dc;
  --band-top:#ffffff;
  --band-bottom:#e4e2e6;
  --field:#ffffff;
}
*{box-sizing:border-box;margin:0;padding:0}
html,body{width:1040px;height:1200px;overflow:hidden;background:#fff}
body{position:relative;font-family:"Arimo",Arial,sans-serif;color:var(--text)}
.abs{position:absolute}
.heading{font-family:"Questrial",sans-serif;color:var(--navy);font-weight:400;letter-spacing:1.5px}
.sub{font-family:"Questrial",sans-serif;color:var(--navy-soft);font-size:12px;letter-spacing:1px}

/* header */
.brand{display:flex;align-items:center;gap:10px;font-family:"Questrial",sans-serif;color:var(--navy);font-size:24px;letter-spacing:4px;text-transform:uppercase}
.brand-mark{width:14px;height:14px;border-radius:50%;background:var(--navy);flex:none}
.header-brand{left:91px;top:58px}
.call{right:89px;top:18px;font-family:"Questrial",sans-serif;color:var(--navy);font-size:18px;letter-spacing:1px}
.call span{color:#9aa0aa;font-size:19px}
.search{left:747px;top:54px;width:203px;height:27px;border:1px solid #cfcfd4;border-radius:4px;background:linear-gradient(#f7f7f8,#eeeef0)}
.search svg{position:absolute;right:8px;top:7px}
.nav{left:327px;top:111px;width:623px;display:flex;justify-content:space-between;align-items:center;list-style:none;font-family:"Questrial",sans-serif;font-size:13px;letter-spacing:.8px;color:var(--navy)}
.nav li.dot{width:5px;height:5px;border-radius:50%;background:#c9c9cd}
.nav li.active{color:var(--orange)}

/* hero */
.hero{left:0;top:146px;width:1040px;height:316px;background:linear-gradient(90deg,#d9dde3 0%,#c9ced6 22%,#eef0f2 45%,#e5d9cf 62%,#d8cfc8 78%,#e6e9ee 100%)}
.hero-title{left:109px;top:242px;font-family:"Exo 2",sans-serif;font-weight:700;font-size:20px;letter-spacing:1.5px;color:var(--orange)}
.hero-sub{left:109px;top:270px;font-family:"Questrial",sans-serif;font-size:15px;letter-spacing:1.4px;color:#3b3f48}
.hero-more{left:463px;top:299px;font-family:"Questrial",sans-serif;font-size:11px;letter-spacing:1px;color:#111}

/* intro band */
.band{left:0;top:466px;width:1040px;height:230px;background:linear-gradient(var(--band-top),var(--band-bottom));border-bottom:1px solid var(--line)}
.col-head{font-size:19px}
.divider{width:1px;height:126px;top:537px;background:linear-gradient(rgba(180,180,188,0),#bfbfc6,rgba(180,180,188,0))}
.bullets{left:90px;top:549px;list-style:none;font-family:"Questrial",sans-serif;font-size:11px;letter-spacing:.4px;color:var(--navy)}
.bullets li{position:relative;padding-left:17px;line-height:17.3px}
.bullets li::before{content:"";position:absolute;left:2px;top:7px;width:5px;height:5px;border-radius:50%;background:var(--orange)}
.about-text{left:540px;top:540px;width:155px;font-family:"Questrial",sans-serif;font-size:11px;line-height:15.6px;letter-spacing:.3px;color:var(--navy)}
.puzzle{left:435px;top:533px;width:95px;height:88px;background:linear-gradient(135deg,#f4f4f4,#c9c9cc 60%,#e8e8ea);border:1px solid #e0e0e3}
.btn{display:flex;align-items:center;justify-content:center;border:1px solid #b9b9be;border-radius:3px;background:linear-gradient(#f6f6f7,#d3d3d7);box-shadow:0 1px 2px rgba(0,0,0,.18);font-family:"Arimo",sans-serif;font-size:12px;color:#3b3f48}
.field{left:743px;width:194px;height:21px;border:1px solid #c8c8ce;border-radius:11px;background:var(--field);font-family:"Arimo",sans-serif;font-size:9px;color:#7c8290;padding-left:9px;line-height:19px}

/* feature */
.feature-head{left:89px;top:730px;font-size:19px;padding-bottom:4px;border-bottom:1px dotted #7c8496;width:375px}
.feature-photo{left:88px;top:771px;width:233px;height:198px;background:linear-gradient(135deg,#d6dce3,#b5bcc6 45%,#e9e3de 70%,#cfd3d9)}
.feature-text{left:339px;top:776px;width:343px;font-family:"Questrial",sans-serif;font-size:11px;line-height:17.3px;letter-spacing:.3px;color:var(--navy)}

/* news */
.news-head{left:731px;top:723px;font-size:19px}
.news{left:731px;width:220px;border-bottom:1px solid #cfcfd4;padding-bottom:8px}
.news-date{display:flex;align-items:center;gap:12px;font-family:"Questrial",sans-serif;font-size:10px;color:var(--navy)}
.news-title{font-family:"Arimo",sans-serif;font-weight:700;font-size:11.5px;color:var(--navy);margin-top:4px;letter-spacing:.3px}
.news-body{font-family:"Arimo",sans-serif;font-size:10px;line-height:15.5px;color:var(--muted);margin-top:2px}
.news-more{text-align:right;font-family:"Arimo",sans-serif;font-size:9.5px;color:var(--orange);letter-spacing:.4px}

/* footer */
.footer{left:0;top:1011px;width:1040px;height:150px;background:linear-gradient(#ffffff,#e8e7ea);border-top:1px solid var(--line);border-bottom:1px solid var(--line)}
.footer-brand{left:96px;top:1062px;font-size:18px;letter-spacing:3px}
.footer-brand .brand-mark{width:11px;height:11px}
.fcol{top:1025px;font-family:"Arimo",sans-serif}
.fcol h4{font-size:12px;font-weight:700;color:#2b2f38;margin-bottom:9px;letter-spacing:.3px}
.fcol ul{list-style:none;font-size:9.5px;line-height:15.6px;color:var(--navy);letter-spacing:.4px}
.fdiv{top:1027px;height:108px;border-left:1px dashed #9a9aa2}
.social{display:flex;gap:6px;margin-top:8px}
.social span{width:14px;height:14px;background:#7d8fae;border-radius:2px}
.copyright{left:0;top:1178px;width:1040px;text-align:center;font-family:"Arimo",sans-serif;font-size:9.5px;color:#3b3f48;letter-spacing:.3px}
</style>
</head>
<body>

<header>
  <div class="abs brand header-brand"><span class="brand-mark"></span>Corvane Partners</div>
  <div class="abs call"><span>call us:</span>+1 555 014 2290</div>
  <div class="abs search">
    <svg width="11" height="11" viewBox="0 0 11 11"><circle cx="4.5" cy="4.5" r="3.3" fill="none" stroke="#333" stroke-width="1.4"/><line x1="7" y1="7" x2="10.3" y2="10.3" stroke="#333" stroke-width="1.6"/></svg>
  </div>
  <ul class="abs nav">
    <li class="active">Home</li><li class="dot"></li>
    <li>Our company</li><li class="dot"></li>
    <li>Our Approach</li><li class="dot"></li>
    <li>Our Services</li><li class="dot"></li>
    <li>Our Clients</li><li class="dot"></li>
    <li>Contact</li>
  </ul>
</header>

<section>
  <div class="abs hero" role="img" aria-label="Office photograph of a smiling businesswoman resting her chin on her hands at a desk"></div>
  <div class="abs hero-title">Praesent vestibulum aenean nonummy</div>
  <div class="abs hero-sub">ummy hendrerit mauris. Hasellus porta. Fusce suscipit</div>
  <div class="abs hero-more">More Details...</div>
</section>

<section>
  <div class="abs band"></div>

  <h2 class="abs heading col-head" style="left:90px;top:494px">Why Us ?</h2>
  <div class="abs sub" style="left:90px;top:518px">Hasellus porta. Fusce suscipit</div>
  <ul class="abs bullets">
    <li>Lorem Ipsum has been the industry's standard dummy.</li>
    <li>since the 1500s, when an unknown printer took a galley.</li>
    <li>Scrambled it to make a type specimen book.</li>
    <li>It has survived not only five centuries, but also the leap</li>
  </ul>
  <div class="abs btn" style="left:143px;top:646px;width:184px;height:26px">Click here to get started !</div>

  <div class="abs divider" style="left:414px"></div>

  <h2 class="abs heading col-head" style="left:440px;top:496px">Who Are We ?</h2>
  <div class="abs puzzle" role="img" aria-label="Illustration of white jigsaw puzzle pieces"></div>
  <p class="abs about-text">India is fast catching up and the availability of power has a huge impact on the eco-nomic growth. In the last years, the country has mas-</p>
  <div class="abs btn" style="left:452px;top:646px;width:183px;height:26px">Get to know more about us !</div>

  <div class="abs divider" style="left:718px"></div>

  <h2 class="abs heading col-head" style="left:745px;top:494px">Get Your Quote</h2>
  <div class="abs sub" style="left:746px;top:517px">Hasellus porta. Fusce suscipit</div>
  <div class="abs field" style="top:547px">First Name</div>
  <div class="abs field" style="top:574px">Last Name</div>
  <div class="abs field" style="top:601px">E mail</div>
  <div class="abs btn" style="left:786px;top:640px;width:96px;height:25px">Send</div>
</section>

<section>
  <h2 class="abs heading feature-head">Lorem ipsum dolor sit amet consecdi.</h2>
  <div class="abs feature-photo" role="img" aria-label="Photograph of three business colleagues working together at a laptop"></div>
  <p class="abs feature-text">Scing elraesent ves tibm moeaean onummy hendrerit mauris. Phasellus portauspit varius misociis ulus mus. Nulla dui. Fusce feu-giat malesuada odio. Morbi nio gravida atcursus necuus a loree-nas tristique orci ac sem. Duis ultricies pharetra magna. Donec acumsan<br>malesuada orcinec sit amet eros. Lorem ipsum dolor sit am con-sectetuer adipiscing eliuris fermentum dictum magna. Sed oreet aliquam leo. [+].</p>
  <div class="abs btn" style="left:341px;top:928px;width:95px;height:26px">Read More</div>

  <h2 class="abs heading news-head">Recent News</h2>
  <article class="abs news" style="top:763px">
    <div class="news-date">
      <svg width="17" height="17" viewBox="0 0 17 17"><rect x="1" y="2.5" width="15" height="13.5" rx="1.5" fill="#fff" stroke="#4d5f82"/><rect x="1" y="2.5" width="15" height="4" fill="#7d8fae"/><text x="8.5" y="14" font-size="6" font-family="Arial" font-weight="700" text-anchor="middle" fill="#1f3763">24</text></svg>
      September,24
    </div>
    <div class="news-title">Hasellus porta. Fusce suscipit</div>
    <div class="news-body">India is fast catching up and the availability of power has a huge impact on the economic</div>
    <div class="news-more">read more</div>
  </article>
  <article class="abs news" style="top:868px">
    <div class="news-date">
      <svg width="17" height="17" viewBox="0 0 17 17"><rect x="1" y="2.5" width="15" height="13.5" rx="1.5" fill="#fff" stroke="#4d5f82"/><rect x="1" y="2.5" width="15" height="4" fill="#7d8fae"/><text x="8.5" y="14" font-size="6" font-family="Arial" font-weight="700" text-anchor="middle" fill="#1f3763">24</text></svg>
      September,24
    </div>
    <div class="news-title">Hasellus porta. Fusce suscipit</div>
    <div class="news-body">India is fast catching up and the availability of power has a huge impact on the economic</div>
    <div class="news-more">read more</div>
  </article>
</section>

<footer>
  <div class="abs footer"></div>
  <div class="abs brand footer-brand"><span class="brand-mark"></span>Corvane</div>

  <div class="abs fdiv" style="left:257px"></div>
  <div class="abs fcol" style="left:270px"><h4>Company</h4><ul><li>About Us</li><li>Sitemap</li><li>Website Terms</li><li>Terms of Business</li><li>Privacy Policy</li></ul></div>
  <div class="abs fdiv" style="left:378px"></div>
  <div class="abs fcol" style="left:410px"><h4>Product</h4><ul><li>Business Websites</li><li>Reviews</li><li>Quick Tour</li><li>Pricing</li><li>Free Trial</li></ul></div>
  <div class="abs fdiv" style="left:517px"></div>
  <div class="abs fcol" style="left:550px"><h4>Internet financing</h4><ul><li>Financing Tips</li><li>Search Optimisation</li><li>Social Media</li><li>Video Marketing</li><li>Business Cases</li></ul></div>
  <div class="abs fdiv" style="left:681px"></div>
  <div class="abs fcol" style="left:727px"><h4>Services</h4><ul><li>Help/Contact us</li><li>Business directory</li><li>Legal notices</li><li>Privacy policy</li><li>Terms &amp; Conditions</li></ul></div>
  <div class="abs fdiv" style="left:837px"></div>
  <div class="abs fcol" style="left:868px"><h4 style="margin-left:9px">Follow us</h4>
    <div class="social" aria-label="Social links"><span></span><span></span><span></span><span></span></div>
  </div>

  <div class="abs copyright">Copyright © 2012 Meridel Communications Company. All rights reserved.</div>
</footer>

</body>
</html>
```